Park furniture company needs a new product flyer

We're a street and park furniture supply company and we have a new range of furniture that we would like to showcase to prospective customers.
Pictures, logo and copy attached.
Furniture pictures are also available with a black background.
Warranty information needs to feature on the flyer.
Recycled content information needs to feature on the flyer.

Target Market(s)

Landscape Architects

Font styles to use
Serif

Requirements
Must have
• Professional fonts and graphics.
Should not have
• comic sans or similar fonts - cheap graphics

```html
<!DOCTYPE html>
<html lang="en">
<head>
<meta charset="UTF-8">
<title>Avenue Grove – Product Flyer</title>
<link href="https://fonts.googleapis.com/css2?family=Montserrat:wght@300;700&family=Open+Sans:wght@400&family=Oswald:wght@500;600&display=swap" rel="stylesheet">
<style>
  :root{
    --blue:#1f74bf;
    --red:#c41e24;
    --red-dark:#9e1a1f;
    --charcoal:#4a4b4d;
    --ink:#1f1f1f;
    --paper:#ffffff;
    --mist:#eceef1;
    --frame:#b9b9b9;
    --timber:#a9522a;
    --timber-dark:#6e3a1f;
    --alloy:#b8aa92;
  }
  *{margin:0;padding:0;box-sizing:border-box}
  html,body{width:960px;height:1200px;overflow:hidden;background:var(--paper)}
  .flyer{position:relative;width:960px;height:1200px;overflow:hidden;
    background:linear-gradient(135deg,var(--mist) 0%,var(--paper) 45%,var(--mist) 100%);
    font-family:'Open Sans',sans-serif;color:var(--ink)}
  .brand{position:absolute;left:84px;top:88px;font-family:'Montserrat',sans-serif;
    font-weight:700;font-size:50px;letter-spacing:1px;color:var(--charcoal);line-height:1}
  .hero-band{position:absolute;left:0;top:198px;width:720px;height:300px;background:var(--blue)}
  .headline{position:absolute;left:69px;top:232px;font-family:'Montserrat',sans-serif;
    font-weight:300;font-size:35px;line-height:45px;color:var(--paper)}
  .headline b{font-weight:700}
  .headline .closing{font-size:42px;font-weight:700;display:block;margin-top:2px}
  .warranty-band{position:absolute;left:0;top:498px;width:700px;height:87px;
    background:linear-gradient(90deg,var(--red),var(--red-dark))}
  .warranty-box{position:absolute;left:71px;top:483px;width:533px;height:89px;
    border:2px solid var(--paper);display:flex;align-items:center;justify-content:center;
    font-family:'Oswald',sans-serif;font-weight:600;font-size:60px;color:var(--paper);letter-spacing:1px}
  .hero-product{position:absolute;left:620px;top:71px;width:293px;height:518px;
    background:linear-gradient(180deg,var(--timber) 0%,var(--timber-dark) 55%,var(--alloy) 100%)}
  .thumbs{position:absolute;left:84px;top:610px;width:258px}
  .thumb{height:155px;margin-bottom:21px;border:9px solid var(--frame);background:var(--paper);
    padding:10px;box-shadow:0 8px 10px rgba(0,0,0,.15)}
  .thumb-fill{width:100%;height:100%;
    background:linear-gradient(180deg,var(--timber-dark) 0%,var(--alloy) 100%)}
  .thumb-fill.bench{background:linear-gradient(180deg,var(--timber) 0%,var(--timber-dark) 60%,var(--alloy) 100%)}
  .features{position:absolute;left:463px;top:630px;width:460px;list-style:none}
  .features li{display:flex;gap:11px;font-size:15px;line-height:21px;margin-bottom:12px;white-space:nowrap}
  .features li.compact{font-size:13.5px;line-height:19px;margin-bottom:15px}
  .features svg{flex:0 0 13px;margin-top:4px}
  .call-bar{position:absolute;left:0;top:1065px;width:960px;height:66px}
  .call-text{position:absolute;left:472px;top:1065px;height:66px;display:flex;align-items:center;gap:14px;
    font-family:'Oswald',sans-serif;font-weight:600;font-size:42px;color:var(--paper)}
  .info-bar{position:absolute;left:0;top:1131px;width:960px;height:69px;background:var(--blue);
    display:flex;align-items:center;justify-content:center;gap:14px;
    font-family:'Oswald',sans-serif;font-weight:500;font-size:35px;color:var(--paper)}
</style>
</head>
<body>
<div class="flyer">
  <div class="brand">AVENUE GROVE</div>

  <div class="hero-band"></div>
  <div class="hero-product" role="img" aria-label="Product photo: timber-slat bench seat with backrest and beige aluminium frame armrests"></div>
  <p class="headline">European <b>inspired</b><br>with a <b>unique</b> and<br><b>original design</b>, that is<br>functional all while respecting<span class="closing">the Environment.</span></p>

  <div class="warranty-band"></div>
  <div class="warranty-box">10-YEAR WARRANTY</div>

  <div class="thumbs">
    <div class="thumb"><div class="thumb-fill" role="img" aria-label="Product photo: bench seat and table set"></div></div>
    <div class="thumb"><div class="thumb-fill bench" role="img" aria-label="Product photo: bench with backrest and armrests, front view"></div></div>
    <div class="thumb"><div class="thumb-fill" role="img" aria-label="Product photo: table with two bench seats"></div></div>
  </div>

  <ul class="features">
    <li><svg width="13" height="13" viewBox="0 0 14 14"><circle cx="7" cy="7" r="6" fill="none" stroke="#1f74bf" stroke-width="1.3"/><path d="M4 7.2l2 2 4-4" fill="none" stroke="#1f74bf" stroke-width="1.3"/></svg><span>Our range is designed to make life easier for<br>people; created using extremely durable, ultra low<br>maintenance materials.</span></li>
    <li><svg width="13" height="13" viewBox="0 0 14 14"><circle cx="7" cy="7" r="6" fill="none" stroke="#1f74bf" stroke-width="1.3"/><path d="M4 7.2l2 2 4-4" fill="none" stroke="#1f74bf" stroke-width="1.3"/></svg><span>Featuring 98% recycled composite battens in a<br>range of stain and fade-resistant colour options and a<br>unique aluminium frame design.</span></li>
    <li><svg width="13" height="13" viewBox="0 0 14 14"><circle cx="7" cy="7" r="6" fill="none" stroke="#1f74bf" stroke-width="1.3"/><path d="M4 7.2l2 2 4-4" fill="none" stroke="#1f74bf" stroke-width="1.3"/></svg><span>The capped composite battens come with a 10-year<br>commercial warranty covering staining, fading and<br>structural performance.</span></li>
    <li><svg width="13" height="13" viewBox="0 0 14 14"><circle cx="7" cy="7" r="6" fill="none" stroke="#1f74bf" stroke-width="1.3"/><path d="M4 7.2l2 2 4-4" fill="none" stroke="#1f74bf" stroke-width="1.3"/></svg><span>Site-specific for healthcare applications offering<br>wheelchair accessibility options</span></li>
    <li class="compact"><svg width="13" height="13" viewBox="0 0 14 14"><circle cx="7" cy="7" r="6" fill="none" stroke="#1f74bf" stroke-width="1.3"/><path d="M4 7.2l2 2 4-4" fill="none" stroke="#1f74bf" stroke-width="1.3"/></svg><span>The Avenue Grove range comprises of a seat with optional<br>armrests, bench seat and table, available in both standard or<br>DDA designs.</span></li>
    <li class="compact"><svg width="13" height="13" viewBox="0 0 14 14"><circle cx="7" cy="7" r="6" fill="none" stroke="#1f74bf" stroke-width="1.3"/><path d="M4 7.2l2 2 4-4" fill="none" stroke="#1f74bf" stroke-width="1.3"/></svg><span>Uniform length of 1800mm with tailored options available.</span></li>
    <li class="compact"><svg width="13" height="13" viewBox="0 0 14 14"><circle cx="7" cy="7" r="6" fill="none" stroke="#1f74bf" stroke-width="1.3"/><path d="M4 7.2l2 2 4-4" fill="none" stroke="#1f74bf" stroke-width="1.3"/></svg><span>Bolt down or freestanding options.</span></li>
  </ul>

  <svg class="call-bar" viewBox="0 0 960 66" preserveAspectRatio="none"><polygon points="441,0 960,0 960,66 401,66" fill="#4a4b4d"/></svg>
  <div class="call-text">
    <span>CALL US</span>
    <svg width="44" height="44" viewBox="0 0 44 44"><circle cx="22" cy="22" r="21" fill="#1f74bf"/><circle cx="22" cy="22" r="16" fill="#ffffff"/><path d="M16 13c1.5-1 2.5-.5 3.3 1l1.6 3c.6 1.2.2 2-1 2.7l-1 .6c.8 2.4 2.4 4.3 4.6 5.5l.7-1c.8-1.1 1.6-1.3 2.7-.6l2.8 1.9c1.3.9 1.4 2 .3 3.3-1.8 2.1-4.4 2-7.3.3-4.2-2.5-7.200-6.4-8.2-10.6-.6-2.6 0-4.6 1.5-6.1z" fill="#1f74bf"/></svg>
    <span>0987 654 321</span>
  </div>

  <div class="info-bar">
    <span>FOR MORE INFORMATION VISIT</span>
    <svg width="34" height="34" viewBox="0 0 34 34" fill="none" stroke="#ffffff" stroke-width="2"><circle cx="17" cy="17" r="15"/><ellipse cx="17" cy="17" rx="7" ry="15"/><path d="M2 17h30M5 9h24M5 25h24"/></svg>
    <span>WWW.AVENUEGROVE.COM.AU</span>
  </div>
</div>
</body>
</html>
```